Business Card for Lumina Nest

I need a very attractive business card as per the logo..

lumina nest is a centre providing services to pregnant women...

DR. Karim Haddadi

Consultant-  Maternal Fetal Medicine & Director of Lumina Nest Center

Kingdom of Saudi Arabia

Tel : +966 1 57 3 8164

Fax : +966 1 57 3 9275

khaddadi@luminest-example.com

www.luminanest-example.com

Target Market(s)

the target market is the pregnant women and women having issues with pregnancy or with babies

Industry/Entity Type

Business

Requirements
Must have
• the business card will be in English and Arabic..........one we finalize the design maybe on the back u can place Arabic..of in the front one side may be Arabic one side english

```html
<!DOCTYPE html>
<html lang="en">
<head>
<meta charset="utf-8">
<title>Lumina Nest – Business Card</title>
<link rel="stylesheet" href="https://fonts.googleapis.com/css2?family=Ubuntu:wght@400;500;700&display=swap">
<style>
  :root {
    --backdrop: #ececec;
    --card-white: #fbfbfb;
    --pink: #e8899e;
    --pink-light: #f6c3ce;
    --pink-deep: #e07891;
    --teal: #5ccdb8;
    --teal-soft: #9fe3d5;
    --white: #ffffff;
  }
  * { box-sizing: border-box; margin: 0; padding: 0; }
  html, body {
    width: 1200px;
    height: 493px;
    overflow: hidden;
    background: var(--backdrop);
    font-family: "Ubuntu", sans-serif;
  }
  .stage {
    position: relative;
    width: 1200px;
    height: 493px;
  }
  .card {
    position: absolute;
    top: 96px;
    width: 525px;
    height: 300px;
    border-radius: 3px;
    box-shadow: 0 2px 6px rgba(0,0,0,0.08);
    overflow: hidden;
  }

  /* Back of card */
  .card-back {
    left: 50px;
    background: radial-gradient(circle at 65% 35%, var(--pink-light) 0%, var(--pink) 70%, var(--pink-deep) 100%);
    color: var(--white);
  }
  .card-back .brand-block {
    position: absolute;
    left: 50%;
    top: 50%;
    transform: translate(-50%, -50%);
    white-space: nowrap;
  }
  .card-back .website {
    display: block;
    font-size: 15px;
    font-weight: 500;
    margin-left: 60px;
    margin-bottom: 2px;
    letter-spacing: 0.3px;
    white-space: nowrap;
  }
  .brand {
    display: flex;
    align-items: center;
    gap: 12px;
    font-weight: 500;
    white-space: nowrap;
  }
  .brand-dot {
    border-radius: 50%;
    flex: none;
  }
  .card-back .brand { font-size: 40px; }
  .card-back .brand-dot {
    width: 46px; height: 46px;
    border: 4px solid var(--white);
  }

  /* Front of card */
  .card-front {
    left: 625px;
    background: var(--card-white);
  }
  .card-front .brand {
    position: absolute;
    left: 26px;
    top: 34px;
    font-size: 32px;
    color: var(--teal);
  }
  .card-front .brand-dot {
    width: 40px; height: 40px;
    border: 4px solid var(--pink);
  }
  .swirl-motif {
    position: absolute;
    right: -20px;
    top: 0;
    width: 260px;
    height: 300px;
    background: radial-gradient(closest-side circle at 55% 55%, var(--teal) 0%, var(--teal-soft) 50%, var(--pink-light) 78%, rgba(251,251,251,0) 100%);
  }
  .person {
    position: absolute;
    left: 26px;
    top: 136px;
  }
  .person-name {
    font-size: 24px;
    font-weight: 700;
    color: var(--teal);
    white-space: nowrap;
  }
  .person-title {
    margin-top: 6px;
    font-size: 11px;
    line-height: 1.35;
    color: var(--pink);
    padding-bottom: 8px;
    border-bottom: 1px solid var(--pink-light);
    width: 250px;
    white-space: nowrap;
  }
  .contacts {
    position: absolute;
    left: 26px;
    top: 228px;
    list-style: none;
  }
  .contacts li {
    display: flex;
    align-items: center;
    gap: 10px;
    font-size: 12.5px;
    font-weight: 500;
    color: var(--teal);
    line-height: 21px;
    white-space: nowrap;
  }
  .contacts svg {
    width: 14px;
    height: 14px;
    fill: none;
    stroke: var(--pink);
    stroke-width: 1.6;
    flex: none;
  }
</style>
</head>
<body>
<main class="stage">

  <section class="card card-back" aria-label="Card back">
    <div class="brand-block">
      <span class="website">www.luminanest-example.com</span>
      <div class="brand"><span class="brand-dot"></span>Lumina Nest</div>
    </div>
  </section>

  <section class="card card-front" aria-label="Card front">
    <div class="brand"><span class="brand-dot"></span>Lumina Nest</div>

    <div class="swirl-motif" role="img" aria-label="Decorative teal and pink swirl motif"></div>

    <div class="person">
      <h1 class="person-name">Dr. Karim Haddadi</h1>
      <p class="person-title">Consultant-&nbsp; Maternal Fetal Medicine &amp;<br>Director of Lumina Nest Center</p>
    </div>

    <ul class="contacts">
      <li>
        <svg viewBox="0 0 16 16" aria-hidden="true"><path d="M3 2h3l1.5 3.5-2 1.2a8 8 0 0 0 3.8 3.8l1.2-2L14 10v3a1 1 0 0 1-1 1A11 11 0 0 1 2 3a1 1 0 0 1 1-1z"/></svg>
        +966 1 57 3 8164
      </li>
      <li>
        <svg viewBox="0 0 16 16" aria-hidden="true"><rect x="4" y="1.5" width="8" height="4"/><rect x="1.5" y="5.5" width="13" height="6" rx="1"/><rect x="4" y="9.5" width="8" height="5"/></svg>
        +966 1 57 3 9275
      </li>
      <li>
        <svg viewBox="0 0 16 16" aria-hidden="true"><rect x="1.5" y="3.5" width="13" height="9" rx="1"/><path d="M1.5 4l6.5 5 6.5-5"/></svg>
        khaddadi@luminest-example.com
      </li>
    </ul>
  </section>

</main>
</body>
</html>
```